Corvane Collective Web Presence Design and Relaunch

Take existing web files and "clean up" for a a more presentable web landing pad.
posted presently on a site pad CSS template. at www.corvanecollective.org

The site is clunky and unprofessional looking. Needs to be toned down so the urgency is conveyed, but not via a burning planet image.

Target Market(s)

Non-profit climate adaptation group targeting local government land management agencies, special districts and private landholders of natural resource properties.

Industry/Entity Type

Environment

Coding

Coded - Design and coding required

Number of Pages Required

4 page

Font styles to use
Serif
Sans Serif

Requirements
Must have
• Include current logos, aspects if content on current site www.corvanecollective.org
• A regional Pacific Northwest Focus (US & Canada). Content speaking to urgency but respectful of cultural diversity and norms. Sustainability themes. Emphasis on action and implementation.
Nice to have
• link to like minded projects. Appear to future generations. Diversity in thematic areas ecological resiliency, energy, food security and infrastructure.

```html
<!DOCTYPE html>
<html lang="en">
<head>
<meta charset="utf-8">
<title>Corvane Collective – Implementing Climate Adaptation</title>
<link href="https://fonts.googleapis.com/css2?family=Source+Sans+3:wght@400;500;600&display=swap" rel="stylesheet">
<style>
:root{
  --maroon:#6b0a0a;
  --gold:#8b6a3e;
  --gold-text:#d9a441;
  --ink:#1a1a1a;
  --body:#3a3a3a;
  --line:#e3e1e1;
  --tile:#f4f2f2;
  --footer:#141414;
  --blue:#1c8fc9;
}
*{box-sizing:border-box;margin:0;padding:0}
html,body{width:1200px;height:2516px;overflow:hidden;background:#fff}
body{font-family:"Source Sans 3",sans-serif;color:var(--ink)}
.page{position:relative;width:1200px;height:2516px;overflow:hidden}
.abs{position:absolute}

/* header */
.site-header{left:0;top:0;width:1200px;height:51px;background:#f2f2f2}
.brand{left:233px;top:14px;font-size:15px;font-weight:600;color:var(--maroon);display:flex;align-items:center;gap:6px}
.brand i{width:10px;height:10px;border-radius:50%;background:var(--maroon);display:block}
.nav{right:237px;top:21px;display:flex;gap:22px;font-size:10px;font-weight:500}
.nav a{color:var(--ink);text-decoration:none}
.nav a.active{color:var(--maroon)}

/* hero */
.hero-photo{left:684px;top:51px;width:464px;height:394px;background:radial-gradient(circle at 50% 40%,#5fae3a 0 18%,#e9f2e4 30%,#f3dcd2 55%,#eceef2 80%)}
.hero-copy{left:245px;top:150px;width:400px;text-align:center}
.eyebrow{font-size:14px;color:var(--maroon);font-weight:500}
.hero-copy h1{font-size:30px;font-weight:500;line-height:36px;margin-top:18px}
.hero-copy p{font-size:9px;line-height:15px;color:var(--body);margin-top:28px}

/* section titles */
.sec-title{left:0;width:1200px;text-align:center}
.sec-title h2{display:inline-block;font-size:29px;font-weight:500;padding:0 6px 6px;border-bottom:2px solid var(--gold)}
.lede{left:385px;width:430px;text-align:center;font-size:9.3px;line-height:15px;color:var(--body)}

/* featured */
.featured{left:0;top:445px;width:1200px;height:586px;background:linear-gradient(180deg,#eeeeee 0%,#dcdcdc 45%,#e4e4e4 100%)}
.card{width:357px;height:188px;background:#fff;padding:10px}
.card-inner{border:1px solid var(--line);height:100%;position:relative}
.card-icon{position:absolute;left:22px;top:44px;width:48px;height:48px;border-radius:50%;background:#eeeeee;display:flex;align-items:center;justify-content:center}
.card h3{position:absolute;left:104px;top:28px;font-size:13.5px;font-weight:500;letter-spacing:.2px}
.card p{position:absolute;left:104px;top:57px;width:218px;font-size:9px;line-height:15px;color:var(--body)}

/* stats */
.stat{top:1244px;width:170px;height:141px;background:var(--tile);border:1px solid var(--line);text-align:center;padding-top:22px}
.stat.highlight{background:var(--maroon);border-color:var(--maroon);color:#fff}
.stat svg{display:block;margin:0 auto}
.stat .num{font-size:15px;margin-top:12px;line-height:20px}
.stat .label{font-size:14px;line-height:20px}

/* recent work */
.tile{overflow:hidden}
.tile .ph{position:absolute;inset:0}
.tile .cap{position:absolute;left:0;right:0;bottom:0;height:38px;background:rgba(20,24,30,.6);text-align:center;padding-top:5px}
.cap b{display:block;font-size:11.5px;font-weight:400;color:var(--gold-text);line-height:15px}
.cap span{display:block;font-size:8.5px;color:#eee;line-height:13px}

/* progress */
.bar{left:609px;width:356px;height:25px;background:#efefef}
.bar .fill{position:absolute;left:0;top:0;height:25px;background:var(--maroon);color:#fff;font-size:10px;font-weight:600;padding:6px 0 0 16px}
.bar .pct{position:absolute;top:6px;font-size:10px;font-weight:600;color:var(--maroon)}

/* footer */
.site-footer{left:0;top:2355px;width:1200px;height:161px;background:var(--footer);color:#fff}
.foot-logo{left:234px;top:0;width:168px;height:60px;background:#fff;border-radius:0 0 6px 6px;display:flex;align-items:center;justify-content:center;gap:6px;font-size:15px;font-weight:600;color:var(--blue)}
.foot-logo i{width:10px;height:10px;border-radius:50%;background:var(--blue);display:block}
.foot-name{left:234px;top:76px;width:168px;text-align:center;font-size:17px;font-weight:500;color:var(--blue)}
.foot-tag{left:234px;top:97px;width:168px;text-align:center;font-size:9px;color:#ddd}
.foot-col h4{font-size:10px;font-weight:600;margin-bottom:5px}
.foot-col li{list-style:none;font-size:8.5px;line-height:19px;color:#e5e5e5}
.contact-row{display:flex;align-items:center;gap:10px;font-size:8.5px;color:#e5e5e5;height:19px;margin-bottom:19px}
</style>
</head>
<body>
<div class="page">

  <header class="abs site-header">
    <div class="abs brand"><i></i>Corvane Collective</div>
    <nav class="abs nav"><a class="active" href="#">HOME</a><a href="#">ABOUT</a><a href="#">CONTACT</a></nav>
  </header>

  <div class="abs hero-photo" role="img" aria-label="Cupped hands holding a green globe topped with trees and small houses"></div>
  <section class="abs hero-copy">
    <div class="eyebrow">CLIMATE ADAPTATION</div>
    <h1>Implementing Climate<br>Strategies</h1>
    <p>Dedicated to taking action the Corvane Collective was created to help bring adaption strategies to life. Working with local communities we are committed to implementing strategies that will sustain communities throughout the Pacific Northwest for generations to come.</p>
  </section>

  <section class="abs featured" role="img" aria-label="Misty evergreen forest backdrop">
    <div class="abs sec-title" style="top:44px"><h2>Featured Projects</h2></div>

    <article class="abs card" style="left:234px;top:146px"><div class="card-inner">
      <div class="card-icon"><svg width="22" height="26" viewBox="0 0 22 26" fill="none" stroke="#222" stroke-width="1.3"><rect x="3" y="2" width="16" height="22"/><path d="M6 7h10M6 11h10M6 15h10M6 19h7"/></svg></div>
      <h3>ADAPTATION PLANS</h3>
      <p>Communities throughout the region have adopted plans to to address our changing climate. Many more are in the process of developing plans. We are here to help these communities with the hard work- implementing those plans.</p>
    </div></article>

    <article class="abs card" style="left:607px;top:146px"><div class="card-inner">
      <div class="card-icon"><svg width="22" height="22" viewBox="0 0 22 22" fill="none" stroke="#222" stroke-width="2.2"><path d="M11 2v12M6 9l5 5 5-5M3 19h16"/></svg></div>
      <h3>ON THE GROUND....</h3>
      <p>The Alliance is familiar and growing throughout the region. Presently our work has us on the ground in keystone watersheds in the Cascade, Willamette, Columbia and Boise basin watersheds.</p>
    </div></article>

    <article class="abs card" style="left:234px;top:347px"><div class="card-inner">
      <div class="card-icon"><svg width="24" height="24" viewBox="0 0 24 24" fill="none" stroke="#222" stroke-width="1.3"><path d="M12 20V10M12 12c-4 0-6-3-6-6 4 0 6 3 6 6zM12 11c3 0 5-2 5-5-3 0-5 2-5 5zM4 20c3-3 13-3 16 0"/></svg></div>
      <h3>ECOLOGICAL RESILIENCE</h3>
      <p>To endure change Communities need to keep their watersheds functioning. Our network or professionals have decades of experience understanding and implementing conservation and restoration strategies.</p>
    </div></article>

    <article class="abs card" style="left:607px;top:347px"><div class="card-inner">
      <div class="card-icon"><svg width="24" height="24" viewBox="0 0 24 24" fill="none" stroke="#222" stroke-width="1.3"><path d="M4 11h16l-2 9H6zM8 11l3-6M16 11l-3-6"/><path d="M9 14v4M12 14v4M15 14v4"/></svg></div>
      <h3>ENERGY AND FOOD</h3>
      <p>Security of community food and energy have, and always will be, an essential component of how communities sustain themselves. Beyond the the ecological context managing a minimizing our resource demands will be essential.</p>
    </div></article>
  </section>

  <div class="abs sec-title" style="top:1085px"><h2>What We Are Doing ?</h2></div>
  <p class="abs lede" style="top:1156px">Lorem ipsum dolor sit amet, consectetur adipiscing elit, sed do eiusmod tempor incididunt ut labore et dolore magna aliqua. Ut enim ad minim veniam, quis nostrud exercitation</p>

  <div class="abs stat" style="left:233px">
    <svg width="38" height="46" viewBox="0 0 38 46" fill="none" stroke="#8b6a3e" stroke-width="1.6"><circle cx="19" cy="17" r="14"/><circle cx="19" cy="17" r="9"/><path d="M19 11l2 4 4 .5-3 3 1 4-4-2-4 2 1-4-3-3 4-.5z"/><path d="M10 28l-4 14 6-3 3 5 3-12M28 28l4 14-6-3-3 5-3-12"/></svg>
    <div class="num">250 +</div><div class="label">Projects Completed</div>
  </div>
  <div class="abs stat highlight" style="left:421px">
    <svg width="40" height="44" viewBox="0 0 40 44" fill="none" stroke="#fff" stroke-width="1.6"><path d="M4 14l10-8h14l8 6M36 30l-10 8H12l-8-6"/><rect x="14" y="15" width="12" height="14" rx="2"/><path d="M17 20h6M17 24h6"/></svg>
    <div class="num">300 +</div><div class="label">Donations</div>
  </div>
  <div class="abs stat" style="left:609px">
    <svg width="44" height="44" viewBox="0 0 44 44" fill="none" stroke="#8b6a3e" stroke-width="1.6"><path d="M22 4l10 4v9c0 7-5 11-10 13-5-2-10-6-10-13V8z"/><path d="M22 11l2 4 4 .5-3 3 1 4-4-2-4 2 1-4-3-3 4-.5z"/><path d="M6 18c0 10 7 18 16 20 9-2 16-10 16-20"/></svg>
    <div class="num">17 +</div><div class="label">Communities engaged</div>
  </div>
  <div class="abs stat" style="left:796px">
    <svg width="40" height="44" viewBox="0 0 40 44" fill="#8b6a3e"><circle cx="20" cy="7" r="5"/><path d="M4 6l4-2 8 10h8l8-10 4 2-10 14v22h-5V30h-2v12h-5V20z"/></svg>
    <div class="num">70 +</div><div class="label">Volunteers</div>
  </div>

  <div class="abs sec-title" style="top:1439px"><h2>Recent Work</h2></div>
  <p class="abs lede" style="top:1510px">Lorem ipsum dolor sit amet, consectetur adipiscing elit, sed do eiusmod tempor incididunt ut labore et dolore magna aliqua. Ut enim ad minim veniam, quis nostrud exercitation</p>

  <figure class="abs tile" style="left:234px;top:1581px;width:232px;height:229px">
    <div class="ph" role="img" aria-label="Wind turbine against a sunset sky over mountains" style="background:linear-gradient(180deg,#7d8797 0%,#c9a28c 55%,#e7a26a 75%,#2b1d18 100%)"></div>
    <figcaption class="cap"><b>Energy</b><span>Investing in clean energy</span></figcaption>
  </figure>
  <figure class="abs tile" style="left:234px;top:1825px;width:232px;height:106px">
    <div class="ph" role="img" aria-label="Green seedling held in an open hand" style="background:linear-gradient(160deg,#2d4d2a,#7fb34a 45%,#a7b8c3 70%,#2d3a2a)"></div>
    <figcaption class="cap"><b>Energy</b><span>Investing in clean energy</span></figcaption>
  </figure>
  <figure class="abs tile" style="left:485px;top:1581px;width:229px;height:166px">
    <div class="ph" role="img" aria-label="Hand placing blue sky pieces onto a grey stormy sky" style="background:linear-gradient(120deg,#9a9a9a 0%,#6f6f6f 40%,#3f78d6 65%,#6fa0e0 100%)"></div>
    <figcaption class="cap"><b>Food Security</b><span>Retooling agriculture/span&gt;</span></figcaption>
  </figure>
  <figure class="abs tile" style="left:485px;top:1765px;width:229px;height:166px">
    <div class="ph" role="img" aria-label="Aerial view of a braided river delta and wetlands" style="background:linear-gradient(180deg,#a9b7c4 0%,#9a7a52 35%,#c9b294 55%,#6e5a40 100%)"></div>
    <figcaption class="cap"><b>Ecological Resilience</b><span>Environmental Progress</span></figcaption>
  </figure>
  <figure class="abs tile" style="left:734px;top:1581px;width:231px;height:350px">
    <div class="ph" role="img" aria-label="Hand holding a phone framing a tree-lined road with cars" style="background:linear-gradient(90deg,#2f3a2e 0%,#55604f 30%,#6b6b6b 50%,#55604f 70%,#2f3a2e 100%)"></div>
    <figcaption class="cap"><b>Infrastructure</b><span>Investing in clean energy</span></figcaption>
  </figure>

  <div class="abs sec-title" style="top:1984px"><h2>Think Green ! Save Money</h2></div>
  <div class="abs" role="img" aria-label="Power plant cooling towers releasing steam under a cloudy sky" style="left:234px;top:2075px;width:357px;height:213px;background:linear-gradient(180deg,#7d9bc0 0%,#d8cfc6 40%,#b48a63 70%,#5b4636 100%)"></div>

  <div class="abs bar" style="top:2099px"><div class="fill" style="width:326px">Clean Water</div><span class="pct" style="left:331px">98%</span></div>
  <div class="abs bar" style="top:2143px"><div class="fill" style="width:206px">Forest Rescue</div><span class="pct" style="left:274px">56%</span></div>
  <div class="abs bar" style="top:2188px"><div class="fill" style="width:281px">Agriculture</div><span class="pct" style="left:305px">77%</span></div>
  <div class="abs bar" style="top:2232px"><div class="fill" style="width:294px">Alternative Energy</div><span class="pct" style="left:311px">98%</span></div>

  <footer class="abs site-footer">
    <div class="abs foot-logo"><i></i>Corvane Collective</div>
    <div class="abs foot-name">Corvane Collective</div>
    <div class="abs foot-tag">Implementing Climate Adaptation</div>
    <div class="abs foot-col" style="left:547px;top:25px">
      <h4>LINKS</h4>
      <ul><li>About Us</li><li>Causes</li><li>Testimonial</li><li>Events</li><li>Contact Us</li></ul>
    </div>
    <div class="abs foot-col" style="left:735px;top:25px">
      <h4>CONTACT US</h4>
      <div class="contact-row"><svg width="11" height="11" viewBox="0 0 24 24" fill="#fff"><path d="M6 2l4 5-2 3c1 3 3 5 6 6l3-2 5 4-3 4C10 22 2 14 2 5z"/></svg>360-555-0148</div>
      <div class="contact-row"><svg width="12" height="10" viewBox="0 0 24 18" fill="none" stroke="#fff" stroke-width="2"><rect x="1" y="1" width="22" height="16"/><path d="M1 1l11 9 11-9"/></svg>info@corvanecollective.org</div>
      <div class="contact-row"><svg width="11" height="14" viewBox="0 0 18 24" fill="#fff"><path d="M9 0a9 9 0 0 0-9 9c0 7 9 15 9 15s9-8 9-15a9 9 0 0 0-9-9zm0 13a4 4 0 1 1 0-8 4 4 0 0 1 0 8z"/></svg>418 Alder Row, Harrow Bay WA 98000</div>
    </div>
  </footer>

</div>
</body>
</html>
```